London Whisky Bottle Label

BACKGROUND
We are plumbers that have resurrected London's oldest once illicit Gin Distillery Tarvel Wire https://www.clipvonta.example/watch?v=qR8mLx2TwZ1&t=4s
Bought 150yr old derelict bakery & turned it into an office for our plumbing biz....removed dangerous chimney...got sued by a neighbour ..
our lawyers discovered that the original bakers family once made illict gin here (in what is now our office) we tracked down the origianl family ...see pic enclosed....the little boy now in his 90's (Colin Treadle) gave us his family's secret gin recipe and we have now resurrected it. We supply Wexcombe Hall, Hse of Garnets Pellow Grint etc. Now have our 1st London Whisky.
This is NOT scotch whisky...this a brand new category of drink 'English Whisky'
1. traditional whisky style bottle which will have embossed text on as per the sample English Whisky & K T Distillery LONDON
Front label 110mm x 95mm
Rear label 70mm wide and 100mm
Front Text KESTLE
Rear Text KESTLE
Must have a old map of my area London Q27 8JX on rear
Map link https://charts.vendaro.example/view-full/587261093#zoom=6&lat=1477&lon=6570&layers=BT

Target Market(s)

OVER 30's

Font styles to use
Sans Serif

Requirements
Nice to have
• I want an old map on the front of the label....the map have 2 small rivers on it which are very close to my distillery (called The Sallow Run and Corvick Beck, where they meet there a small bridge called Tollerby's Bridge, i would like this shown on the map, is there any tasteful way to add some colour to the historic map ???

```html
<!DOCTYPE html>
<html lang="en">
<head>
<meta charset="utf-8">
<title>Kestle English Whisky – Labels</title>
<link href="https://fonts.googleapis.com/css2?family=Cinzel:wght@500;600&family=Libre+Baskerville&display=swap" rel="stylesheet">
<style>
  :root {
    --page: #ffffff;
    --paper: #d9d6cd;
    --paper-rear: #dcd9cd;
    --claret: #7b1f1f;
    --gold: #c9a43a;
    --gold-light: #f1dc8a;
    --ink: #2a2622;
    --map-light: #e4e1cf;
    --map-dark: #b9b7a0;
  }
  * { box-sizing: border-box; margin: 0; padding: 0; }
  html, body { width: 1200px; height: 1200px; overflow: hidden; background: var(--page); }
  .canvas {
    width: 1200px; height: 1200px;
    display: flex; align-items: center; justify-content: center; gap: 70px;
  }

  /* Front label 110 × 95 mm */
  .front-label {
    position: relative;
    width: 540px; height: 466px;
    background: var(--paper);
    border-top: 6px solid var(--gold);
    border-bottom: 6px solid var(--gold);
    box-shadow: inset 0 3px 0 var(--gold-light), inset 0 -3px 0 var(--gold-light);
  }
  .front-frame {
    position: absolute; inset: 22px 14px;
    border: 2px solid var(--gold);
    outline: 1px solid var(--gold-light);
    outline-offset: -6px;
    display: flex; flex-direction: column; align-items: center; justify-content: center;
  }
  .front-ornament {
    position: absolute; inset: 10px;
    background: radial-gradient(ellipse at center, rgba(255,255,255,0) 45%, rgba(201,180,140,0.18) 100%);
  }
  .brand-name {
    position: relative;
    font-family: "Cinzel", serif;
    font-weight: 600;
    font-size: 84px; line-height: 1;
    color: var(--claret);
    letter-spacing: 4px;
  }
  .category {
    position: relative;
    font-family: "Cinzel", serif; font-weight: 600;
    font-size: 40px; color: var(--claret);
    margin-top: 22px; letter-spacing: 0.5px;
  }
  .maker {
    position: relative;
    font-family: "Cinzel", serif; font-weight: 500;
    font-size: 15px; color: var(--claret);
    margin-top: 22px; letter-spacing: 3px;
  }

  /* Rear label 70 × 100 mm */
  .rear-label {
    position: relative;
    width: 340px; height: 486px;
    background: var(--paper-rear);
    border: 3px solid var(--gold);
    border-radius: 2px;
    padding: 26px 22px 18px;
    display: flex; flex-direction: column; align-items: center;
    text-align: center;
  }
  .rear-brand {
    font-family: "Cinzel", serif; font-weight: 600;
    font-size: 38px; line-height: 1; color: var(--claret);
    letter-spacing: 2px;
  }
  .rear-copy {
    font-family: "Libre Baskerville", serif;
    font-size: 9.5px; line-height: 1.45; color: var(--ink);
    margin-top: 18px;
  }
  .rear-map {
    width: 100%; height: 214px; margin-top: 12px;
    background: linear-gradient(135deg, var(--map-light), var(--map-dark));
  }
  .volume {
    font-family: "Libre Baskerville", serif;
    font-size: 9.5px; color: var(--ink); margin-top: 18px;
  }
  .rear-note {
    font-family: "Libre Baskerville", serif;
    font-size: 9px; line-height: 1.55; color: var(--ink);
    margin-top: 8px; width: 130px;
  }
</style>
</head>
<body>
<main class="canvas">
  <section class="front-label" aria-label="Front label">
    <div class="front-frame">
      <div class="front-ornament" role="img" aria-label="Faint engraved scroll ornament background"></div>
      <h1 class="brand-name">KESTLE</h1>
      <p class="category">ENGLISH WHISKY</p>
      <p class="maker">KT DISTILLERY LONDON</p>
    </div>
  </section>

  <section class="rear-label" aria-label="Rear label">
    <h2 class="rear-brand">KESTLE</h2>
    <p class="rear-copy">Lorem ipsum dolor sit amet, consectetuer adipiscing elit, sed diam nonummy nibh euismod tincidunt ut laoreet dolore magna aliquam erat volutpat. Ut wisi enim ad minim veniam, quis</p>
    <div class="rear-map" role="img" aria-label="Historic map of the distillery area around Q27 8JX, showing The Sallow Run, Corvick Beck and Tollerby's Bridge"></div>
    <p class="volume">800 ML</p>
    <p class="rear-note">Lorem ipsum dolor sit amet, consectetuer adipiscing elit, sed diam nonummy nibh euismod</p>
  </section>
</main>
</body>
</html>
```